Business Card for By Karel Voss

Looking to have a business card designed for my lifestyle and fitness company. My company offers personal training, online programming and nutrition advice based out of London, United Kingdom.

I'd like to see modern, sleek designs, focusing on black, matte black or matte grey. Design doesn't need to be overly descriptive as this will also be used as a personal business card. I've included my logo.

Please note that my company is no longer called "By Karel Voss" but instead "By Karel Voss", this is because of my other ventures. Therefore please don't use the "fitness by karel voss" text.

information about my company can be found at www.bykarelvoss.com

Company is also based out of London (United Kingdom) & Sydney (Australia) this could be reflected on the card.

Industry/Entity Type

Business

Contact Information for Business Card

Karel Voss
+44 7382 615027
karel@bykarelvoss.com
www.bykarelvoss.com

Font styles to use
Sans Serif

Requirements
Must have
• All contact details and inclusion of my logo.

```html
<!DOCTYPE html>
<html lang="en">
<head>
<meta charset="utf-8">
<title>Karel Voss – Business Card</title>
<link rel="stylesheet" href="https://fonts.googleapis.com/css2?family=Arimo:wght@400;700&display=swap">
<style>
  :root {
    --backdrop: #2b2b2d;
    --card: #1c1c1e;
    --card-edge: #161617;
    --mark-faint: #262628;
    --ink: #ffffff;
    --ink-soft: #d9d9d9;
  }
  * { margin: 0; padding: 0; box-sizing: border-box; }
  html, body {
    width: 1200px; height: 1189px; overflow: hidden;
    background: var(--backdrop);
    font-family: "Arimo", Arial, sans-serif;
  }
  .stage { position: relative; width: 1200px; height: 1189px; }
  .card {
    position: absolute; width: 760px; height: 434px;
    background: linear-gradient(160deg, #232325 0%, var(--card) 55%, var(--card-edge) 100%);
    border-radius: 26px; overflow: hidden;
    box-shadow: 0 18px 40px rgba(0,0,0,.45);
  }
  .card--front { left: 110px; top: 100px; }
  .card--back  { left: 330px; top: 640px; }

  .faint-name {
    position: absolute; color: var(--mark-faint);
    font-weight: 700; line-height: 1; letter-spacing: 1px;
    white-space: nowrap; text-transform: uppercase;
  }
  .card--front .faint-name {
    left: 0; right: 0; top: 280px; text-align: center; font-size: 88px;
  }
  .card--back .faint-name { right: 40px; top: 150px; font-size: 120px; }

  .brand {
    position: absolute; display: flex; align-items: center; gap: 14px;
    color: var(--ink); font-weight: 700; text-transform: uppercase;
  }
  .brand__dot { width: 18px; height: 18px; border-radius: 50%; background: var(--ink); flex: none; }
  .brand__name { font-size: 34px; letter-spacing: 1px; line-height: 1.1; }
  .card--front .brand { left: 50%; top: 110px; transform: translateX(-50%); }
  .card--back .brand { left: 50px; top: 60px; }
  .card--back .brand__name { font-size: 30px; }

  .holder {
    position: absolute; left: 50px; top: 228px;
    color: var(--ink); font-weight: 700; font-size: 24px; letter-spacing: .5px;
  }
  .contacts { position: absolute; left: 50px; top: 282px; list-style: none; }
  .contacts li {
    display: flex; align-items: center; gap: 14px;
    color: var(--ink-soft); font-size: 21px; margin-bottom: 12px;
  }
  .contacts svg { width: 26px; height: 26px; flex: none; }
</style>
</head>
<body>
<main class="stage">
  <section class="card card--front" aria-label="Card front">
    <div class="faint-name" aria-hidden="true">Karel Voss</div>
    <div class="brand">
      <span class="brand__dot"></span>
      <span class="brand__name">By<br>Karel Voss</span>
    </div>
  </section>

  <section class="card card--back" aria-label="Card back">
    <div class="faint-name" aria-hidden="true">Voss</div>
    <div class="brand">
      <span class="brand__dot"></span>
      <span class="brand__name">By<br>Karel Voss</span>
    </div>
    <p class="holder">KAREL VOSS</p>
    <ul class="contacts">
      <li>
        <svg viewBox="0 0 26 26" aria-hidden="true"><circle cx="13" cy="13" r="12" fill="#fff"/><path d="M9 7l3 3-2 2c1 2 2 3 4 4l2-2 3 3-2 2c-5 0-10-5-10-10z" fill="#1c1c1e"/></svg>
        <span>+44 7382 615027</span>
      </li>
      <li>
        <svg viewBox="0 0 26 26" aria-hidden="true"><circle cx="13" cy="13" r="12" fill="#fff"/><rect x="7" y="9" width="12" height="8" fill="none" stroke="#1c1c1e" stroke-width="1.6"/><path d="M7 9l6 5 6-5" fill="none" stroke="#1c1c1e" stroke-width="1.6"/></svg>
        <span>karel@bykarelvoss.com</span>
      </li>
      <li>
        <svg viewBox="0 0 26 26" aria-hidden="true"><circle cx="13" cy="13" r="12" fill="#fff"/><circle cx="13" cy="13" r="6.5" fill="none" stroke="#1c1c1e" stroke-width="1.4"/><ellipse cx="13" cy="13" rx="3" ry="6.5" fill="none" stroke="#1c1c1e" stroke-width="1.2"/><path d="M6.5 13h13" stroke="#1c1c1e" stroke-width="1.2"/></svg>
        <span>www.bykarelvoss.com</span>
      </li>
    </ul>
  </section>
</main>
</body>
</html>
```